General Power Point Presentation Pack

Hello Designers,

I am after a professional looking Microsoft PowerPoint deck that can be used for our corporate presentations. The pack should include a:

Title Page
Tittle and Content Page
Section Header Sheet
Two Content Page
Title Only Page
Blank Page
Content with Caption Page
Picture with Caption Page

I have included my brand guidelines and colours. I have also included some photos you may be able to use. Can you please ensure the pack has page numbering and that when you print it that it can be printed to full A4 Page.

Industry/Entity Type

Property Development & Construction

Requirements
Must have
• Prefer a white or very light coloured background

```html
<!DOCTYPE html>
<html lang="en">
<head>
<meta charset="utf-8">
<title>Northgate Presentation Pack</title>
<link href="https://fonts.googleapis.com/css2?family=Poppins:wght@500&family=Roboto:wght@400;500;700&display=swap" rel="stylesheet">
<style>
  :root {
    --canvas: #c8cacb;
    --orange: #c9552b;
    --orange-deep: #b9461f;
    --gold: #d3a56b;
    --gold-light: #e8ccA0;
    --cream: #f2ebd7;
    --ink: #4a4a4a;
    --white: #ffffff;
    --mauve: #a894a6;
  }
  * { box-sizing: border-box; margin: 0; padding: 0; }
  html, body { width: 828px; height: 1200px; overflow: hidden; }
  body { background: var(--canvas); font-family: "Roboto", Arial, sans-serif; position: relative; }

  .slide {
    position: absolute; width: 364px; height: 257px;
    background: var(--white); overflow: hidden;
    box-shadow: 0 1px 3px rgba(0,0,0,.18);
  }
  .col-left { left: 41px; }
  .col-right { left: 424px; }
  .row-1 { top: 47px; }
  .row-2 { top: 331px; }
  .row-3 { top: 614px; }
  .row-4 { top: 903px; }

  .fill { position: absolute; inset: 0; }
  .brand {
    font-family: "Poppins", Arial, sans-serif; font-weight: 500;
    color: var(--orange); letter-spacing: .2px;
  }
  .brand-footer { position: absolute; left: 10px; bottom: 6px; font-size: 8px; }
  .page-tab {
    position: absolute; right: 0; bottom: 0; width: 26px; height: 9px;
    background: var(--gold); color: var(--white); font-size: 3.6px;
    display: flex; align-items: center; justify-content: center;
    clip-path: polygon(3px 0, 100% 0, 100% 100%, 0 100%);
  }

  /* Title banner */
  .banner { position: absolute; left: 0; top: 0; width: 240px; height: 30px; }
  .banner-title {
    position: absolute; left: 11px; top: 4px; color: var(--white);
    font-weight: 500; font-size: 13px; letter-spacing: .2px;
  }

  .heading { color: var(--gold); font-weight: 500; font-size: 10px; letter-spacing: .2px; }
  .body-copy { color: var(--ink); font-size: 4.5px; line-height: 1.38; text-align: justify; }
  .body-copy p + p { margin-top: 4px; }

  /* Cover */
  .cover-photo { background: linear-gradient(160deg, #c0532b 0%, #c85a2f 55%, #b94e27 100%); }
  .cover-name {
    position: absolute; left: 0; right: 0; top: 150px; text-align: center;
    color: var(--gold-light); font-size: 30px;
  }
  .cover-band {
    position: absolute; left: 0; right: 0; bottom: 0; height: 26px; background: var(--white);
  }
  .cover-tagline {
    position: absolute; left: 14px; top: 9px; font-size: 6.6px; font-weight: 500; color: var(--gold);
  }
  .cover-web {
    position: absolute; right: 0; top: 0; width: 92px; height: 26px;
    background: var(--gold); color: var(--white); font-size: 7px; font-weight: 500;
    display: flex; align-items: center; justify-content: center; gap: 3px;
    clip-path: polygon(8px 0, 100% 0, 100% 100%, 0 100%);
  }

  /* Contents */
  .contents-tab {
    position: absolute; right: 0; top: 17px; width: 74px; height: 17px;
    background: var(--gold); color: var(--white); font-size: 6.5px; font-weight: 500;
    letter-spacing: 2px; display: flex; align-items: center; justify-content: center;
  }
  .contents-item { position: absolute; width: 170px; }
  .contents-item .heading { font-size: 6px; }
  .contents-item .body-copy { text-align: left; }
  .contents-num {
    position: absolute; width: 16px; height: 16px; background: var(--gold);
    color: var(--white); font-size: 5px; display: flex; align-items: center; justify-content: center;
    clip-path: polygon(4px 0, 100% 0, calc(100% - 4px) 100%, 0 100%);
  }

  /* Section header */
  .header-photo { background: linear-gradient(120deg, #c9552b 0%, #cc7538 55%, #c99454 100%); }
  .header-text {
    position: absolute; left: 0; right: 0; top: 145px; text-align: center;
    color: var(--white); font-weight: 700; font-size: 22px;
  }

  /* Title only */
  .title-centre {
    position: absolute; left: 150px; top: 140px; color: var(--white); font-weight: 500; font-size: 14px;
  }
</style>
</head>
<body>

<!-- Title page -->
<section class="slide col-left row-1">
  <div class="fill cover-photo" role="img" aria-label="Apartment buildings on a city street, tinted orange"></div>
  <div class="cover-name brand">Northgate</div>
  <div class="cover-band">
    <span class="cover-tagline">BUILDING OUR FUTURE COMMUNITIES</span>
    <span class="cover-web">
      <svg width="7" height="7" viewBox="0 0 10 10"><circle cx="5" cy="5" r="4.2" fill="none" stroke="#fff" stroke-width="1"/><ellipse cx="5" cy="5" rx="1.8" ry="4.2" fill="none" stroke="#fff" stroke-width=".8"/><line x1=".8" y1="5" x2="9.2" y2="5" stroke="#fff" stroke-width=".8"/></svg>
      northgatehomes.com
    </span>
  </div>
</section>

<!-- Contents page -->
<section class="slide col-right row-1">
  <svg class="fill" width="364" height="257" viewBox="0 0 364 257">
    <polygon points="0,0 163,0 103,257 0,257" fill="#c4552c"/>
  </svg>
  <div class="fill" role="img" aria-label="Trees and apartment blocks, tinted orange" style="clip-path: polygon(0 0,163px 0,103px 100%,0 100%); background: linear-gradient(180deg,#c7592e,#bb4c25);"></div>
  <div class="brand brand-footer" style="color:#fff; left:20px;">Northgate</div>
  <div class="contents-tab">CONTENT</div>

  <div class="contents-num" style="left:157px; top:80px;">1</div>
  <div class="contents-item" style="left:178px; top:77px;">
    <div class="heading">CONTENT</div>
    <div class="body-copy">Project overview, aims and key dates for the year.</div>
  </div>
  <div class="contents-num" style="left:149px; top:113px;">2</div>
  <div class="contents-item" style="left:170px; top:110px;">
    <div class="heading">CONTENT</div>
    <div class="body-copy">Project overview, aims and key dates for the year.</div>
  </div>
  <div class="contents-num" style="left:140px; top:148px;">3</div>
  <div class="contents-item" style="left:161px; top:145px;">
    <div class="heading">CONTENT</div>
    <div class="body-copy">Project overview, aims and key dates for the year.</div>
  </div>
  <div class="contents-num" style="left:131px; top:181px;">4</div>
  <div class="contents-item" style="left:152px; top:178px;">
    <div class="heading">CONTENT</div>
    <div class="body-copy">Project overview, aims and key dates for the year.</div>
  </div>
</section>

<!-- Section header -->
<section class="slide col-left row-2">
  <div class="fill header-photo" role="img" aria-label="Apartment buildings and street trees, orange to gold tint"></div>
  <div class="header-text">HEADER SLIDE</div>
</section>

<!-- Title and content (blank body) -->
<section class="slide col-right row-2">
  <svg class="banner" viewBox="0 0 240 30">
    <polygon points="0,0 229,0 223,23 0,23" fill="#c9552b"/>
    <rect x="0" y="24" width="158" height="3" fill="#d3a56b"/>
    <rect x="158" y="24" width="22" height="3" fill="#ecd9bb"/>
  </svg>
  <div class="banner-title">TITLE</div>
  <div class="brand brand-footer">Northgate</div>
  <div class="page-tab">Page 1</div>
</section>

<!-- Title only -->
<section class="slide col-left row-3">
  <div class="fill" style="background: var(--cream);"></div>
  <div class="fill" style="clip-path: polygon(323px 0,100% 0,100% 100%,272px 100%); background: var(--orange);"></div>
  <div class="fill" role="img" aria-label="Modern apartment building with balconies, tinted mauve" style="clip-path: polygon(87px 0,323px 0,272px 100%,27px 100%); background: linear-gradient(180deg,#b29cae,#9e8aa0);"></div>
  <div class="title-centre">TITLE</div>
  <div class="brand brand-footer" style="color:#fff; left:auto; right:16px;">Northgate</div>
</section>

<!-- Content with caption -->
<section class="slide col-right row-3">
  <svg class="banner" viewBox="0 0 240 30">
    <polygon points="0,0 229,0 223,23 0,23" fill="#c9552b"/>
    <rect x="0" y="24" width="158" height="3" fill="#d3a56b"/>
    <rect x="158" y="24" width="22" height="3" fill="#ecd9bb"/>
  </svg>
  <div class="banner-title">CONTENT WITH CAPTION</div>
  <div style="position:absolute; left:127px; top:60px; width:228px;">
    <div class="heading">CONTENT 1</div>
    <div class="body-copy" style="margin-top:4px;">
      <p>Our new residential quarter brings homes, shops and green space together around a shared central park. Each building is planned for light, air and easy access to transport, so families can live, work and meet close to home every day of the week.</p>
      <p>Construction runs in three stages over two years, with careful attention to quality, safety and the needs of neighbours. Local suppliers and trades are used wherever possible to support the wider community.</p>
      <p>Our new residential quarter brings homes, shops and green space together around a shared central park. Each building is planned for light, air and easy access to transport, so families can live, work and meet close to home every day of the week.</p>
    </div>
  </div>
  <div class="brand brand-footer">Northgate</div>
  <div class="page-tab">Page 1</div>
</section>

<!-- Two content -->
<section class="slide col-left row-4">
  <svg class="banner" viewBox="0 0 240 30">
    <polygon points="0,0 229,0 223,23 0,23" fill="#c9552b"/>
    <rect x="0" y="24" width="158" height="3" fill="#d3a56b"/>
    <rect x="158" y="24" width="22" height="3" fill="#ecd9bb"/>
  </svg>
  <div class="banner-title">TWO CONTENT PAGE</div>
  <div style="position:absolute; left:26px; top:58px; width:143px;">
    <div class="heading">CONTENT 1</div>
    <div class="body-copy" style="margin-top:4px;">
      <p>Our new residential quarter brings homes, shops and green space together around a shared central park. Each building is planned for light, air and easy access to transport, so families can live, work and meet close to home every day of the week.</p>
      <p>Construction runs in three stages over two years, with careful attention to quality, safety and the needs of neighbours. Local suppliers and trades are used wherever possible to support the wider community.</p>
      <p>Our new residential quarter brings homes, shops and green space together around a shared central park. Each building is planned for light, air and easy access to transport, so families can live, work and meet close to home every day of the week.</p>
      <p>Sales open in spring, and early buyers will receive a choice of finishes, storage options and parking.</p>
    </div>
  </div>
  <div style="position:absolute; left:192px; top:58px; width:143px;">
    <div class="heading">CONTENT 2</div>
    <div class="body-copy" style="margin-top:4px;">
      <p>Our new residential quarter brings homes, shops and green space together around a shared central park. Each building is planned for light, air and easy access to transport, so families can live, work and meet close to home every day of the week.</p>
      <p>Construction runs in three stages over two years, with careful attention to quality, safety and the needs of neighbours. Local suppliers and trades are used wherever possible to support the wider community.</p>
      <p>Our new residential quarter brings homes, shops and green space together around a shared central park. Each building is planned for light, air and easy access to transport, so families can live, work and meet close to home every day of the week.</p>
      <p>Sales open in spring, and early buyers will receive a choice of finishes, storage options and parking.</p>
    </div>
  </div>
  <div class="brand brand-footer">Northgate</div>
  <div class="page-tab">Page 1</div>
</section>

<!-- Picture with caption -->
<section class="slide col-right row-4">
  <svg class="banner" viewBox="0 0 240 30">
    <polygon points="0,0 229,0 223,23 0,23" fill="#c9552b"/>
    <rect x="0" y="24" width="158" height="3" fill="#d3a56b"/>
    <rect x="158" y="24" width="22" height="3" fill="#ecd9bb"/>
  </svg>
  <div class="banner-title">PICTURE WITH CAPTION</div>
  <div role="img" aria-label="Open-plan kitchen and living room with large windows" style="position:absolute; left:17px; top:46px; width:181px; height:89px; background: linear-gradient(135deg,#d9d2c6,#a7a49a 60%,#8c8a80);"></div>
  <div style="position:absolute; left:210px; top:60px; width:144px;">
    <div class="heading">CONTENT 1</div>
    <div class="body-copy" style="margin-top:4px;"><p>Our new residential quarter brings homes, shops and green space together around a shared central park. Each building is planned for light, air and easy access to transport, so families can live, work and meet close to home every day of the week.</p></div>
  </div>
  <div role="img" aria-label="Apartment living area with dining table and garden view" style="position:absolute; left:172px; top:140px; width:182px; height:89px; background: linear-gradient(135deg,#ddd6ca,#aaa79b 60%,#8a887e);"></div>
  <div style="position:absolute; left:15px; top:157px; width:146px;">
    <div class="heading">CONTENT 2</div>
    <div class="body-copy" style="margin-top:4px;"><p>Our new residential quarter brings homes, shops and green space together around a shared central park. Each building is planned for light, air and easy access to transport, so families can live, work and meet close to home every day of the week.</p></div>
  </div>
  <div class="brand brand-footer">Northgate</div>
  <div class="page-tab">Page 1</div>
</section>

</body>
</html>
```